Develop a PowerPoint template that I can use for my Professional Develoment leadership series.

July 7 – 9:00 AM – Leadership as Core
July 21 – 9:00 AM – Equitable Access
August 4 – 9:00 AM – Academic Pathways
August 18 – 9:00 AM – Robust Student Support
September 1 – 9:00 AM – Connections to Career
September 15 – 9:00 AM – High-Quality and Deep Partnerships

The Leadership series is posted on both the NM and MA websites at http://www.tandelhighprep.com/
http://www.vrqs-lp.com/

I need 2 powerpoints with the same content, just a different look and feel to mirror that of the 2 websites. Please use the color from the two websites and any pictures, etc.

Also, put my company's logo and information in the footer. I am attaching a logo, below is our copyright information:

Copyright © 2020 KB7up™ Bridgeway9Futures™ | All rights reserved

```html
<!DOCTYPE html>
<html lang="en">
<head>
<meta charset="utf-8">
<title>Leadership Series – Presentation Template Styles</title>
<link rel="stylesheet" href="https://fonts.googleapis.com/css2?family=Roboto:ital,wght@0,400;0,500;0,700;0,900;1,400&display=swap">
<style>
:root{
  --navy:#1b3591;
  --gold:#d4a24c;
  --blue-text:#2049b0;
  --teal:#15847f;
  --orange:#f0a43a;
  --ink:#111;
  --muted:#666;
  --page:#fff;
  --line:#dcdcdc;
}
*{margin:0;padding:0;box-sizing:border-box}
html,body{width:1200px;height:831px;overflow:hidden;background:var(--page)}
body{position:relative;font-family:"Roboto",Arial,sans-serif;color:var(--ink)}

.style-heading{position:absolute;left:0;width:1200px;text-align:center;line-height:1}
.style-heading .kicker{font-size:32px;font-weight:400;display:block}
.style-heading .name{font-size:46px;font-weight:900;display:block;margin-top:8px}
.heading-1{top:48px}
.heading-2{top:466px}

.divider{position:absolute;left:46px;top:414px;width:1105px;border-top:1px dashed #999}

.slide{position:absolute;width:351px;height:197px;background:#fff;border:1px solid var(--line);
  box-shadow:0 3px 8px rgba(0,0,0,.12);overflow:hidden}
.row-1{top:162px}.row-2{top:579px}
.col-a{left:46px}.col-b{left:423px}.col-c{left:800px}

.brand{position:absolute;display:flex;align-items:center;gap:2px;font-size:8.5px;font-weight:400;color:#333;line-height:1}
.brand i{display:block;width:6px;height:6px;background:var(--orange)}
.copyright{position:absolute;font-size:3.6px;color:var(--muted);white-space:nowrap}
.page-num{position:absolute;font-size:3.6px;color:var(--muted);right:17px;top:187px}
.foot-brand{left:18px;top:185px}
.foot-copy{left:68px;top:187px}

.slide-title{position:absolute;left:17px;top:19px;font-size:13px;font-weight:700;color:var(--ink);white-space:nowrap}
.title-rule{position:absolute;left:17px;top:37px;width:16px;height:2px;background:var(--navy)}
.bottom-stripe{position:absolute;left:0;bottom:0;height:2px;width:100%;
  background:linear-gradient(90deg,var(--navy) 0 68%,var(--gold) 68% 100%)}
.col-split{position:absolute;left:175px;top:46px;width:1px;height:132px;background:#e2e2e2}

/* Style 1 title slide */
.s1-photo{position:absolute;left:0;top:34px;width:276px;height:93px;
  background:linear-gradient(180deg,#8fb0cf 0%,#b8cde0 45%,#c9b79c 70%,#6f7b6a 100%)}
.s1-band-navy{position:absolute;left:276px;top:34px;width:53px;height:93px;background:var(--navy)}
.s1-band-gold{position:absolute;left:329px;top:34px;width:22px;height:93px;background:var(--gold)}
.s1-title{position:absolute;left:17px;top:140px;font-size:14px;font-weight:700;color:var(--navy);white-space:nowrap}
.deck-date{position:absolute;font-size:5.8px;color:var(--ink)}

/* Seminar blocks */
.sem{position:absolute;width:147px;height:42px}
.sem .txt{position:absolute;line-height:1.05}
.sem .num{font-size:7px;font-weight:700;display:block}
.sem .topic{font-size:5.6px;font-weight:700;display:block}
.sem .desc{font-size:3.8px;display:block;margin-top:1px;color:#222}
.sem1{left:17px}.sem2{left:187px}
.r1{top:46px}.r2{top:90px}.r3{top:134px}

.s1 .date-bar{position:absolute;left:0;top:0;width:147px;height:8px;background:var(--navy);
  color:#fff;font-size:4.6px;font-weight:700;padding:2px 3px;line-height:1}
.s1 .ico{position:absolute;left:1px;top:13px;width:18px;height:18px}
.s1 .txt{left:22px;top:11px;width:124px}
.s1 .num{color:var(--navy)}

.s2 .rule{position:absolute;left:35px;top:0;width:112px;height:1px;background:var(--teal)}
.s2 .rule::after{content:"";position:absolute;right:-1px;top:-1px;width:3px;height:3px;border-radius:50%;background:var(--teal)}
.s2 .ico{position:absolute;left:0;top:0;width:32px;height:32px;border-radius:50%;background:var(--teal)}
.s2 .txt{left:36px;top:3px;width:110px}
.s2 .when{font-size:4.4px;font-weight:500;color:var(--orange);display:block}
.s2 .num{color:var(--teal)}

/* Presenter slides */
.intro{position:absolute;left:17px;top:65px;width:172px;font-size:6.6px;line-height:1.3;color:var(--blue-text)}
.goal-h{position:absolute;left:18px;top:128px;font-size:9.5px;font-weight:700}
.goal-p{position:absolute;left:18px;top:141px;width:160px;font-size:5.8px;font-style:italic;line-height:1.3}
.s1-person{position:absolute;top:65px;width:67px;height:94px;background:linear-gradient(160deg,#b49b80,#6b5746)}
.s1-person.p2{background:linear-gradient(160deg,#a9a59c,#55575c)}
.s1-person .tag{position:absolute;left:0;bottom:0;width:100%;height:11px;background:var(--navy);color:#fff;
  font-size:5.6px;font-weight:700;text-align:center;line-height:11px}
.pa{left:195px}.pb{left:266px}

/* Style 2 */
.s2-photo{position:absolute;inset:0;
  background:radial-gradient(ellipse 75% 120% at 100% 50%,#f1efea 0 55%,rgba(241,239,234,0) 75%),
  linear-gradient(100deg,#9a7356 0%,#c9a988 25%,#d9d2c4 45%,#c7c4b8 100%)}
.s2-brand{right:18px;top:18px}
.s2-title{position:absolute;left:190px;top:91px;font-size:14px;font-weight:700;color:var(--teal);line-height:1.1}
.s2-copy{left:17px;top:187px;color:#fff}
.half-dot{position:absolute;left:-9px;top:18px;width:18px;height:18px;border-radius:50%;background:var(--teal)}
.s2-rule{position:absolute;left:17px;width:160px;height:1px;background:#222}
.s2-rule::after{content:"";position:absolute;right:-1px;top:-1px;width:3px;height:3px;border-radius:50%;background:#222}
.s2-intro{top:71px;width:160px;color:var(--teal)}
.s2-rule.a{top:62px;background:var(--teal)}
.s2-rule.a::after{background:var(--teal)}
.s2-rule.b{top:126px}
.s2-person{position:absolute;top:71px;width:67px;height:67px;border-radius:50%;background:linear-gradient(160deg,#b49b80,#6b5746)}
.s2-person.p2{background:linear-gradient(160deg,#a9a59c,#55575c)}
.s2-name{position:absolute;top:143px;width:67px;text-align:center;font-size:5.8px;font-weight:700;color:var(--teal)}
</style>
</head>
<body>

<svg width="0" height="0" style="position:absolute">
  <defs>
    <symbol id="i-people" viewBox="0 0 24 24"><g fill="none" stroke="currentColor" stroke-width="1.4"><circle cx="12" cy="7" r="3"/><path d="M6 20v-3a6 6 0 0 1 12 0v3"/><circle cx="4.5" cy="10" r="2"/><circle cx="19.5" cy="10" r="2"/></g></symbol>
    <symbol id="i-person" viewBox="0 0 24 24"><g fill="none" stroke="currentColor" stroke-width="1.4"><circle cx="12" cy="7" r="4"/><path d="M5 21v-3a7 7 0 0 1 14 0v3"/></g></symbol>
    <symbol id="i-path" viewBox="0 0 24 24"><g fill="none" stroke="currentColor" stroke-width="1.4"><circle cx="6" cy="8" r="2.5"/><path d="M3 21v-6a3 3 0 0 1 6 0v6M10 14h5v-4h5M18 4v6"/></g></symbol>
    <symbol id="i-career" viewBox="0 0 24 24"><g fill="none" stroke="currentColor" stroke-width="1.4"><rect x="3" y="11" width="18" height="10" rx="1"/><path d="M9 11V8h6v3M3 15h18"/></g></symbol>
    <symbol id="i-hand" viewBox="0 0 24 24"><g fill="none" stroke="currentColor" stroke-width="1.4"><path d="M2 11l4-4 5 3 3-2 4 3 4-2M6 13l4 4 2-1 2 2 3-3 2 1"/></g></symbol>
  </defs>
</svg>

<h1 class="style-heading heading-1"><span class="kicker">Powerpoint Template</span><span class="name">Style 1</span></h1>

<!-- Style 1: title -->
<section class="slide row-1 col-a">
  <div class="brand" style="left:19px;top:17px"><i></i>KB7up</div>
  <div class="s1-photo" role="img" aria-label="Photo of a modern campus building with a wind turbine"></div>
  <div class="s1-band-navy"></div><div class="s1-band-gold"></div>
  <h2 class="s1-title">Presentation Template Guideline</h2>
  <p class="deck-date" style="left:17px;top:161px">JULY 2020</p>
  <p class="copyright" style="left:17px;top:186px">Copyright © 2020 KB7up™ Bridgeway9Futures™ | All rights reserved</p>
</section>

<!-- Style 1: schedule -->
<section class="slide row-1 col-b s1">
  <h2 class="slide-title">Summer Early College Leadership Series</h2>
  <div class="title-rule"></div>
  <div class="col-split"></div>
  <div class="sem sem1 r1"><div class="date-bar">JULY 7</div><svg class="ico" style="color:var(--navy)"><use href="#i-people"/></svg>
    <div class="txt"><span class="num">SEMINAR 1</span><span class="topic">Leadership as Core to Early College Programs</span><span class="desc">In this first seminar, participants will network to share, discuss, and strengthen results-based leadership skills.</span></div></div>
  <div class="sem sem1 r2"><div class="date-bar">JULY 21</div><svg class="ico" style="color:var(--navy)"><use href="#i-people"/></svg>
    <div class="txt"><span class="num">SEMINAR 2</span><span class="topic">Equitable Access</span><span class="desc">In this session, our focus will be on engaging underrepresented students in higher education.</span></div></div>
  <div class="sem sem1 r3"><div class="date-bar">AUGUST 4</div><svg class="ico" style="color:var(--navy)"><use href="#i-path"/></svg>
    <div class="txt"><span class="num">SEMINAR 3</span><span class="topic">Guided Academic Pathways</span><span class="desc">Integrating and aligning academic pathways with college and career will be the topic of our third seminar.</span></div></div>
  <div class="sem sem2 r1"><div class="date-bar">AUGUST 18</div><svg class="ico" style="color:var(--navy)"><use href="#i-person"/></svg>
    <div class="txt"><span class="num">SEMINAR 4</span><span class="topic">Enhanced Student Support</span><span class="desc">Discussion focuses on research and best practice to support students in both academics and advising.</span></div></div>
  <div class="sem sem2 r2"><div class="date-bar">SEPTEMBER 1</div><svg class="ico" style="color:var(--navy)"><use href="#i-career"/></svg>
    <div class="txt"><span class="num">SEMINAR 5</span><span class="topic">Connection to Career</span><span class="desc">In this seminar, the topic centers around connecting students to careers through workplace and experiential learning.</span></div></div>
  <div class="sem sem2 r3"><div class="date-bar">SEPTEMBER 15</div><svg class="ico" style="color:var(--navy)"><use href="#i-hand"/></svg>
    <div class="txt"><span class="num">SEMINAR 6</span><span class="topic">Effective Partnerships</span><span class="desc">Leadership in today's highly complex environment requires the ability to develop strong, collaborative partnerships between high schools and colleges. Understanding and building accountability within these partnerships will be the focus of our final session.</span></div></div>
  <div class="brand foot-brand"><i></i>KB7up</div>
  <p class="copyright foot-copy">Copyright © 2020 KB7up™ Bridgeway9Futures™ | All rights reserved</p>
  <p class="page-num">2</p>
  <div class="bottom-stripe"></div>
</section>

<!-- Style 1: presenters -->
<section class="slide row-1 col-c">
  <h2 class="slide-title">Summer Early College Leadership Series</h2>
  <div class="title-rule"></div>
  <p class="intro">Join Marcus Ellery, J.D. and Dr. Daniel Prewitt as they facilitate virtual seminars with experienced early college leaders. Each of the six, hour-long seminars focuses on important principles of early college design and will be interactive, with discussion around research and best practice.</p>
  <h3 class="goal-h">The goal:</h3>
  <p class="goal-p">To develop a professional learning community where participants support and learn from one another.</p>
  <div class="s1-person pa" role="img" aria-label="Portrait photo of Marcus Ellery"><span class="tag">Marcus Ellery, J.D</span></div>
  <div class="s1-person pb p2" role="img" aria-label="Portrait photo of Dr. Daniel Prewitt"><span class="tag">Dr. Daniel Prewitt</span></div>
  <div class="brand foot-brand"><i></i>KB7up</div>
  <p class="copyright foot-copy">Copyright © 2020 KB7up™ Bridgeway9Futures™ | All rights reserved</p>
  <p class="page-num">3</p>
  <div class="bottom-stripe"></div>
</section>

<div class="divider"></div>

<h1 class="style-heading heading-2"><span class="kicker">Powerpoint Template</span><span class="name">Style 2</span></h1>

<!-- Style 2: title -->
<section class="slide row-2 col-a">
  <div class="s2-photo" role="img" aria-label="Photo of a smiling student holding a book on a sunny campus"></div>
  <div class="brand s2-brand"><i></i>KB7up</div>
  <h2 class="s2-title">Presentation<br>Template Guideline</h2>
  <p class="deck-date" style="left:190px;top:128px">JULY 2020</p>
  <p class="copyright s2-copy">Copyright © 2020 KB7up™ Bridgeway9Futures™ | All rights reserved</p>
</section>

<!-- Style 2: schedule -->
<section class="slide row-2 col-b s2">
  <div class="half-dot"></div>
  <h2 class="slide-title">Summer Leadership Series</h2>
  <div class="col-split"></div>
  <div class="sem sem1 r1"><div class="rule"></div><svg class="ico" style="color:#fff;padding:7px"><use href="#i-people"/></svg>
    <div class="txt"><span class="when">JULY 7</span><span class="num">SEMINAR 1</span><span class="topic">Leadership as Core to Early College Programs</span><span class="desc">In this first seminar, participants will network to share, discuss, and strengthen results-based leadership skills.</span></div></div>
  <div class="sem sem1 r2"><div class="rule"></div><svg class="ico" style="color:#fff;padding:7px"><use href="#i-people"/></svg>
    <div class="txt"><span class="when">JULY 21</span><span class="num">SEMINAR 2</span><span class="topic">Equitable Access</span><span class="desc">In this session, our focus will be on engaging underrepresented students in higher education.</span></div></div>
  <div class="sem sem1 r3"><div class="rule"></div><svg class="ico" style="color:#fff;padding:7px"><use href="#i-path"/></svg>
    <div class="txt"><span class="when">AUGUST 4</span><span class="num">SEMINAR 3</span><span class="topic">Guided Academic Pathways</span><span class="desc">Integrating and aligning academic pathways with college and career will be the topic of our third seminar.</span></div></div>
  <div class="sem sem2 r1"><div class="rule"></div><svg class="ico" style="color:#fff;padding:7px"><use href="#i-person"/></svg>
    <div class="txt"><span class="when">AUGUST 18</span><span class="num">SEMINAR 4</span><span class="topic">Enhanced Student Support</span><span class="desc">Discussion focuses on research and best practice to support students in both academics and advising.</span></div></div>
  <div class="sem sem2 r2"><div class="rule"></div><svg class="ico" style="color:#fff;padding:7px"><use href="#i-career"/></svg>
    <div class="txt"><span class="when">SEPTEMBER 1</span><span class="num">SEMINAR 5</span><span class="topic">Connection to Career</span><span class="desc">In this seminar, the topic centers around connecting students to careers through workplace and experiential learning.</span></div></div>
  <div class="sem sem2 r3"><div class="rule"></div><svg class="ico" style="color:#fff;padding:7px"><use href="#i-hand"/></svg>
    <div class="txt"><span class="when">SEPTEMBER 15</span><span class="num">SEMINAR 6</span><span class="topic">Effective Partnerships</span><span class="desc">Leadership in today's highly complex environment requires the ability to develop strong, collaborative partnerships between high schools and colleges. Understanding and building accountability within these partnerships will be the focus of our final session.</span></div></div>
  <div class="brand foot-brand"><i></i>KB7up</div>
  <p class="copyright foot-copy">Copyright © 2020 KB7up™ Bridgeway9Futures™ | All rights reserved</p>
  <p class="page-num">2</p>
</section>

<!-- Style 2: presenters -->
<section class="slide row-2 col-c">
  <div class="half-dot"></div>
  <h2 class="slide-title">Summer Early College Leadership Series</h2>
  <div class="s2-rule a"></div>
  <p class="intro s2-intro">Join Marcus Ellery, J.D. and Dr. Daniel Prewitt as they facilitate virtual seminars with experienced early college leaders. Each of the six, hour-long seminars focuses on important principles of early college design and will be interactive, with discussion around research and best practice.</p>
  <div class="s2-rule b"></div>
  <h3 class="goal-h" style="top:131px">The goal:</h3>
  <p class="goal-p" style="top:144px">To develop a professional learning community where participants support and learn from one another.</p>
  <div class="s2-person" style="left:195px" role="img" aria-label="Round portrait photo of Marcus Ellery"></div>
  <div class="s2-person p2" style="left:266px" role="img" aria-label="Round portrait photo of Dr. Daniel Prewitt"></div>
  <p class="s2-name" style="left:195px">Marcus Ellery, J.D</p>
  <p class="s2-name" style="left:266px">Dr. Daniel Prewitt</p>
  <div class="brand foot-brand"><i></i>KB7up</div>
  <p class="copyright foot-copy">Copyright © 2020 KB7up™ Bridgeway9Futures™ | All rights reserved</p>
  <p class="page-num">3</p>
</section>

</body>
</html>
```